Design a business card
Business name: Harborline Growth Consulting
Improving Business Profitibility

- An Overview of the Business & Service:

Business Performance Consulting

- The Target Market: Small to medium-sized business

- Design Specifics:
White card, blue ink, moon eclipse

No Logo

Target Market(s)

Small to medium-sized business

Font styles to use
Sans Serif

```html
<!DOCTYPE html>
<html lang="en">
<head>
<meta charset="utf-8">
<title>Harborline Growth Consulting – Business Card</title>
<link href="https://fonts.googleapis.com/css2?family=Roboto:wght@400;700&display=swap" rel="stylesheet">
<style>
  :root {
    --page-bg: #e9e9ee;
    --card-white: #ffffff;
    --ink-navy: #2b2768;
    --ink-soft: #4a4690;
    --moon-light: #f2f2fb;
    --moon-mid: #c9c8ee;
    --moon-deep: #9f9dd8;
  }
  html, body {
    margin: 0;
    width: 1200px;
    height: 905px;
    overflow: hidden;
    background: var(--page-bg);
    font-family: "Roboto", Arial, sans-serif;
  }
  .business-card {
    position: absolute;
    left: 100px;
    top: 167px;
    width: 1000px;
    height: 571px;
    background: var(--card-white);
    border-radius: 40px;
    box-shadow: 0 10px 30px rgba(0,0,0,0.18);
    overflow: hidden;
  }
  .holder {
    position: absolute;
    right: 80px;
    top: 70px;
    text-align: right;
    color: var(--ink-navy);
  }
  .holder-name {
    font-size: 30px;
    font-weight: 700;
    text-transform: uppercase;
    letter-spacing: 0.5px;
    margin: 0;
  }
  .holder-role {
    font-size: 19px;
    font-weight: 400;
    margin: 2px 18px 0 0;
  }
  .moon-art {
    position: absolute;
    left: 70px;
    top: 175px;
    width: 430px;
    height: 360px;
  }
  .brand-name {
    position: absolute;
    left: 110px;
    top: 295px;
    width: 350px;
    margin: 0;
    color: var(--ink-navy);
    font-size: 44px;
    font-weight: 700;
    line-height: 1.05;
    text-transform: uppercase;
  }
  .contact-icons {
    position: absolute;
    right: 70px;
    top: 290px;
    text-align: right;
    color: var(--ink-navy);
    font-size: 19px;
    line-height: 30px;
  }
  .contact-row {
    display: flex;
    justify-content: flex-end;
    align-items: center;
    gap: 10px;
  }
  .contact-row svg { width: 18px; height: 18px; fill: var(--ink-navy); }
  .contact-repeat {
    position: absolute;
    left: 525px;
    top: 400px;
    color: var(--ink-navy);
    font-size: 19px;
    line-height: 28px;
  }
</style>
</head>
<body>
  <div class="business-card">
    <div class="holder">
      <p class="holder-name">Gordon R Maitland</p>
      <p class="holder-role">Business consultant</p>
    </div>

    <svg class="moon-art" viewBox="0 0 430 360" role="img" aria-label="Full moon photograph in soft lavender tones">
      <defs>
        <radialGradient id="moonGlow" cx="40%" cy="35%" r="70%">
          <stop offset="0%" stop-color="var(--moon-light)"/>
          <stop offset="60%" stop-color="var(--moon-mid)"/>
          <stop offset="100%" stop-color="var(--moon-deep)"/>
        </radialGradient>
      </defs>
      <ellipse cx="215" cy="180" rx="212" ry="178" fill="url(#moonGlow)"/>
    </svg>

    <p class="brand-name">Harborline Growth Consulting</p>

    <div class="contact-icons">
      <div class="contact-row">555-014-0101
        <svg viewBox="0 0 24 24" aria-hidden="true"><path d="M6.6 10.8a15 15 0 0 0 6.6 6.6l2.2-2.2c.3-.3.7-.4 1-.2 1.1.4 2.3.6 3.6.6.6 0 1 .4 1 1V20c0 .6-.4 1-1 1A17 17 0 0 1 3 4c0-.6.4-1 1-1h3.5c.6 0 1 .4 1 1 0 1.3.2 2.5.6 3.6.1.3 0 .7-.2 1z"/></svg>
      </div>
      <div class="contact-row">info@harborlinegrowth.com
        <svg viewBox="0 0 24 24" aria-hidden="true"><path d="M2 5h20v14H2z M3 6l9 7 9-7" fill="none" stroke="var(--ink-navy)" stroke-width="2"/></svg>
      </div>
      <div class="contact-row">harborlinegrowth.com
        <svg viewBox="0 0 24 24" aria-hidden="true"><g fill="none" stroke="var(--ink-navy)" stroke-width="1.8"><circle cx="12" cy="12" r="9"/><ellipse cx="12" cy="12" rx="4" ry="9"/><path d="M3 12h18M5 7h14M5 17h14"/></g></svg>
      </div>
    </div>

    <div class="contact-repeat">
      <div>info@harborlinegrowth.com</div>
      <div>harborlinegrowth.com</div>
    </div>
  </div>
</body>
</html>
```